Business Card Design for a Handbags business

We are modernising our handbags website (see attached file for new front page) and are in need of a modern business card and a related design we can use on a small marquee at the markets, on letterhead, emails etc.

As the leather handbags we mostly import are from Italy, we want a smart modern European feel to the design. We are currently thinking about changing the name of the business from Meadowlark Handbags (see www.meadowlarkhandbags.com.au) to Vantera Handbags. Also open to other suggestions you may have that communicates the European influence and quality.

Target Market(s)

25-65 year old women (and some men)

Industry/Entity Type

Business

Contact Information for Business Card

Single or double sided - whichever creates more of an impact

Font styles to use
Serif
Sans Serif

Requirements
Must have
• Clean crisp look, slightly Italian or European look and feel to reflect where the handbags are imported from
Nice to have
• open to ideas

```html
<!DOCTYPE html>
<html lang="en">
<head>
<meta charset="utf-8">
<title>Vantera Handbags – Business Card</title>
<link rel="stylesheet" href="https://fonts.googleapis.com/css2?family=Cinzel:wght@400;500&family=Tinos&display=swap">
<style>
  :root {
    --stage: #1c1c1c;
    --card: #0a0a0a;
    --card-edge: #2a2a2a;
    --white: #f4f4f4;
    --grey: #9a9a9a;
    --red: #d7262e;
  }
  * { box-sizing: border-box; margin: 0; padding: 0; }
  html, body {
    width: 1200px; height: 873px; overflow: hidden;
    background: var(--stage);
  }
  .stage { position: relative; width: 1200px; height: 873px; }

  .card {
    position: absolute;
    width: 540px; height: 310px;
    background: var(--card);
    border: 1px solid var(--card-edge);
    border-radius: 18px;
    color: var(--white);
    overflow: hidden;
  }
  .card--front { left: 50px; top: 150px; }
  .card--back  { left: 610px; top: 412px; }

  /* Front */
  .front-mark {
    position: absolute; left: 50%; top: 62px;
    width: 96px; height: 96px; margin-left: -48px;
    border: 3px solid var(--red); border-radius: 50%;
  }
  .brand {
    font-family: "Cinzel", serif;
    font-weight: 400;
    color: var(--white);
    letter-spacing: 1px;
    white-space: nowrap;
  }
  .tagline {
    font-family: "Cinzel", serif;
    color: var(--grey);
    letter-spacing: 6px;
    white-space: nowrap;
  }
  .front-lockup {
    position: absolute; left: 0; right: 0; top: 178px;
    text-align: center;
  }
  .front-lockup .brand { font-size: 30px; }
  .front-lockup .tagline { font-size: 13px; margin-top: 2px; }

  /* Back */
  .back-lockup { position: absolute; left: 34px; top: 40px; }
  .back-lockup .brand { font-size: 28px; }
  .back-lockup .tagline { font-size: 12px; margin-top: 1px; }

  .rule {
    position: absolute; left: 200px; right: 40px; top: 190px;
    height: 1px; background: var(--white); opacity: .8;
  }
  .person { position: absolute; left: 34px; top: 176px; }
  .person__name {
    font-family: "Cinzel", serif; font-size: 17px; letter-spacing: 1px;
  }
  .person__role {
    font-family: "Tinos", serif; font-size: 14px; color: var(--red);
  }
  .contact-list {
    list-style: none;
    font-family: "Tinos", serif; font-size: 14px;
  }
  .contact-list li { display: flex; align-items: center; gap: 8px; height: 22px; }
  .contact-list--personal { position: absolute; left: 34px; top: 232px; }
  .contact-list--company {
    position: absolute; right: 40px; top: 138px; text-align: right;
  }
  .contact-list--company li { justify-content: flex-end; font-size: 12.5px; }
  .icon { width: 12px; height: 12px; flex: none; }
</style>
</head>
<body>
<main class="stage">

  <section class="card card--front" aria-label="Card front">
    <div class="front-mark" aria-hidden="true"></div>
    <div class="front-lockup">
      <p class="brand">VANTERA HANDBAGS</p>
      <p class="tagline">LUXURY LEATHER HANDBAGS</p>
    </div>
  </section>

  <section class="card card--back" aria-label="Card back">
    <div class="back-lockup">
      <p class="brand">VANTERA HANDBAGS</p>
      <p class="tagline">LUXURY LEATHER HANDBAGS</p>
    </div>

    <ul class="contact-list contact-list--company">
      <li>www.vanterahandbags.com
        <svg class="icon" viewBox="0 0 12 12" aria-hidden="true"><g fill="none" stroke="#d7262e" stroke-width="1"><circle cx="6" cy="6" r="5"/><ellipse cx="6" cy="6" rx="2.2" ry="5"/><line x1="1" y1="6" x2="11" y2="6"/></g></svg>
      </li>
      <li>Kelford, Northbay
        <svg class="icon" viewBox="0 0 12 12" aria-hidden="true"><path d="M6 11.5 C3 7.5 2 6 2 4.2 A4 4 0 0 1 10 4.2 C10 6 9 7.5 6 11.5Z" fill="#d7262e"/><circle cx="6" cy="4.3" r="1.5" fill="#0a0a0a"/></svg>
      </li>
    </ul>

    <div class="rule" aria-hidden="true"></div>

    <div class="person">
      <p class="person__name">CLAUDIA MARSH</p>
      <p class="person__role">Managing Director</p>
    </div>

    <ul class="contact-list contact-list--personal">
      <li>
        <svg class="icon" viewBox="0 0 12 12" aria-hidden="true"><path d="M2.5 1 L4.5 1 L5.3 3.6 L4 4.6 C4.7 6 6 7.3 7.4 8 L8.4 6.7 L11 7.5 L11 9.5 C11 10.4 10.3 11 9.5 11 C5 10.6 1.4 7 1 2.5 C1 1.7 1.6 1 2.5 1Z" fill="#d7262e"/></svg>
        0412 555 309
      </li>
      <li>
        <svg class="icon" viewBox="0 0 12 12" aria-hidden="true"><rect x="0.5" y="2" width="11" height="8" fill="#d7262e"/><path d="M0.8 2.3 L6 6.6 L11.2 2.3" fill="none" stroke="#0a0a0a" stroke-width="1"/></svg>
        claudiamarsh@email.com
      </li>
    </ul>
  </section>

</main>
</body>
</html>
```